Maelis Spacial\floral Decorator

Maelis is a spacial\floral decorator. She is passionate about Art, Life, Architecture, Painting, Music and movement. Her website will be used to showcase her spacial and floral design projects.
We are looking for a very unique website that stands apart from the crowd.
We believe that is achieved through simple high quality design Simple being very important.
The Home page should display primarily photos.
Your task is to provide an un-coded homepage template.
The page must be dynamic in its style and feel.

Maelis has suggest a grid pattern for the images, similar to this http://www.dorvanbloomhouse.co.uk. Overall We like the look and feel of this site.

We like the following color palettes, please base your design around one of them;
https://tintrova.example.com/#themes/search?term=5531704
https://tintrova.example.com/#themes/search?term=5536218
https://tintrova.example.com/#themes/search?term=5548126
https://tintrova.example.com/#themes/search?term=5540967
https://tintrova.example.com/#themes/search?term=5537419

Our target Market is High End Corporate Clients, located in Shanghai and Taipai. For these clients she utilise her floral and interior design skills to decorate a space. See Photos 2, 3 and 21 for examples.
She also targets High End personal clients for events such as weddings and gift combination i.e. flowers and something else.

Requirements
Must have
• Chinese/ English Language Selection
A selection of pictures that appear and disappear.
A menu system that includes:
Home – Portfolio – About Maelis – Blog – Contact Her
A very subtle menu system linking to chatnest, worklinq On, v+ and xunmo.
Nice to have
• We also like the use of an image for the background but this is not necessary.
Should not have
• Alot of Text, yes we now this isn't great for SEO but we will deal with that on other pages

```html
<!DOCTYPE html>
<html lang="en">
<head>
<meta charset="utf-8">
<title>Maelis Floral Design</title>
<link href="https://fonts.googleapis.com/css2?family=Ubuntu:wght@400;500&family=Montserrat:ital,wght@1,800&display=swap" rel="stylesheet">
<style>
:root{
  --page:#d5c99a;
  --card:#ffffff;
  --ink:#7a7048;
  --ink-soft:#8d845e;
  --line:#e4dcc0;
  --accent:#f0c060;
  --button:#8a7e55;
}
*{margin:0;padding:0;box-sizing:border-box}
html,body{width:1200px;height:1159px;overflow:hidden}
body{background:var(--page);font-family:"Ubuntu",sans-serif;color:var(--ink);position:relative}
.abs{position:absolute}
.lang{left:946px;top:31px;width:85px;height:21px;background:#fff;border:1px solid #cfc6a4;border-radius:3px;font-size:10px;display:flex;align-items:center;gap:6px;padding-left:7px;color:#555}
.lang .flag{width:16px;height:11px;background:linear-gradient(135deg,#2a3f8a,#c8303c 50%,#2a3f8a)}
.freephone{right:169px;top:66px;font-size:13px;color:var(--ink-soft)}
.freephone b{font-weight:400;font-size:17px;margin-left:3px}
.card{background:var(--card);border-radius:13px;box-shadow:0 14px 10px -8px rgba(120,105,60,.35)}
.header{left:151px;top:103px;width:899px;height:85px}
.brand{left:33px;top:26px;font-size:28px;color:var(--ink);letter-spacing:.5px}
.nav{right:38px;top:33px;display:flex;gap:37px;font-size:16px;list-style:none}
.hero{left:151px;top:213px;width:898px;height:362px}
.hero-image{left:16px;top:17px;width:864px;height:330px;background:radial-gradient(circle at 30% 40%,#e36fcf 0 12%,transparent 30%),radial-gradient(circle at 70% 30%,#d95fc6 0 14%,transparent 32%),radial-gradient(circle at 85% 75%,#c24fbe 0 10%,transparent 28%),radial-gradient(circle at 15% 80%,#b84bb0 0 12%,transparent 30%),linear-gradient(135deg,#3c8a3a,#cf63c4 35%,#a995d8 70%,#d66ad0)}
.hero-title{left:425px;top:244px;font-family:"Montserrat",sans-serif;font-style:italic;font-weight:800;color:#fff;font-size:50px;line-height:48px;text-align:center;width:290px}
.arrow{top:182px}
.grid{left:151px;width:898px;height:182px}
.tile{position:absolute}
.tile h3{font-weight:400;font-size:16px;color:var(--ink);margin-bottom:8px}
.thumb{width:196px;height:114px;border:1px solid #d3cdb8;border-radius:8px;padding:6px;background:#fff;box-shadow:0 1px 3px rgba(0,0,0,.12)}
.thumb div{width:100%;height:100%}
.footer{left:0;top:1012px;width:1200px;height:130px;background:#fff;border-top:4px solid #fff;box-shadow:inset 0 3px 0 var(--page),inset 0 -4px 0 var(--page)}
.footer .col{top:32px;font-size:13px}
.phone{font-size:21px;color:var(--ink);display:block;margin:2px 0 7px}
.vdiv{top:18px;width:1px;height:104px;background:var(--line)}
.email{width:177px;height:25px;border:1px solid var(--accent);border-radius:3px;font-size:11px;color:#bbb;padding:5px 10px;margin:8px 0 9px}
.signup{width:67px;height:22px;background:var(--button);color:#fff;border-radius:4px;font-size:10px;text-align:center;line-height:22px}
.links{font-size:12px;line-height:26px}
.links span{margin:0 7px;}
.social{display:flex;gap:10px;margin:10px 0 12px;font-size:11px}
.social span{display:flex;align-items:center;gap:4px}
.social i{width:9px;height:9px;background:var(--ink);display:inline-block}
.copy{font-size:12px}
</style>
</head>
<body>
<div class="abs lang"><span class="flag" role="img" aria-label="English flag"></span>English
  <svg width="8" height="6" viewBox="0 0 8 6"><path d="M1 1l3 3 3-3" fill="none" stroke="#444" stroke-width="1.5"/></svg></div>
<div class="abs freephone">Freephone: <b>0800 417 2286</b></div>

<header class="abs card header">
  <div class="abs brand">Maelis Floral Design</div>
  <ul class="abs nav"><li>Home</li><li>Portfolio</li><li>About</li><li>Blog</li><li>Contact Her</li></ul>
</header>

<section class="abs card hero">
  <div class="abs hero-image" role="img" aria-label="Close-up of pink chrysanthemums with green centres"></div>
  <svg class="abs arrow" style="left:64px" width="34" height="70" viewBox="0 0 34 70"><path d="M30 2L6 35l24 33" fill="none" stroke="rgba(235,235,235,.85)" stroke-width="10"/></svg>
  <svg class="abs arrow" style="left:800px" width="34" height="70" viewBox="0 0 34 70"><path d="M4 2l24 33-24 33" fill="none" stroke="rgba(235,235,235,.85)" stroke-width="10"/></svg>
  <div class="abs hero-title">LORE<br>COMMOD</div>
</section>

<section class="abs card grid" style="top:604px">
  <div class="tile" style="left:20px;top:19px"><h3 style="margin-left:3px">Weddings</h3><div class="thumb"><div role="img" aria-label="Pink and white lily bridal bouquet" style="background:radial-gradient(circle at 40% 50%,#d4405e,#f3c9d0 60%,#f5f0f4)"></div></div></div>
  <div class="tile" style="left:239px;top:19px"><h3>Funerals</h3><div class="thumb"><div role="img" aria-label="White lily funeral arrangement" style="background:radial-gradient(ellipse at 50% 70%,#fff 0 25%,#9bb078 45%,#f7ece8 70%)"></div></div></div>
  <div class="tile" style="left:461px;top:19px"><h3>Shop</h3><div class="thumb"><div role="img" aria-label="Buckets of colourful flowers in the shop" style="background:linear-gradient(160deg,#5d7a3c,#c9352c 45%,#e8a030 65%,#6e5a7c)"></div></div></div>
  <div class="tile" style="left:682px;top:19px"><h3>Chocolate Explosion</h3><div class="thumb"><div role="img" aria-label="Bouquet of chocolate bars and ribbons" style="background:linear-gradient(135deg,#6a3a8c,#e0b030 40%,#b0302c 65%,#e9e4ea)"></div></div></div>
</section>

<section class="abs card grid" style="top:807px">
  <div class="tile" style="left:20px;top:21px"><h3>About Us</h3><div class="thumb"><div role="img" aria-label="Flower studio shop front on a high street" style="background:linear-gradient(110deg,#8a8278,#5a5048 40%,#f0c030 60%,#9aa0b0)"></div></div></div>
  <div class="tile" style="left:240px;top:21px"><h3>MK Wedding</h3><div class="thumb"><div role="img" aria-label="Garland of lilac roses" style="background:linear-gradient(150deg,#f2f0f2,#a892d0 40%,#6b8a50 60%,#f2f0f2)"></div></div></div>
  <div class="tile" style="left:462px;top:21px"><h3>Balloons</h3><div class="thumb"><div role="img" aria-label="Couple at a venue decorated with white and yellow balloons" style="background:linear-gradient(180deg,#e8ecee,#c9ccc4 50%,#f0f0d8)"></div></div></div>
  <div class="tile" style="left:683px;top:21px"><h3>Flower Inscription</h3><div class="thumb"><div role="img" aria-label="The word love spelled out in flowers" style="background:linear-gradient(90deg,#fff,#d94060 20%,#e8b030 40%,#5080c0 60%,#d060a0 80%,#fff)"></div></div></div>
</section>

<footer class="abs footer">
  <div class="abs col" style="left:172px">Call Us at the Shop<span class="phone">01632 960471</span>Or Freephone<span class="phone">0800 417 2286</span></div>
  <div class="abs vdiv" style="left:365px"></div>
  <div class="abs col" style="left:391px;font-size:14px">Sign up for Newsletter<div class="email">Email Id</div><div class="signup">Sign Up</div></div>
  <div class="abs vdiv" style="left:589px"></div>
  <div class="abs col links" style="left:613px;top:25px">Home<span>|</span>AboutUs<span>|</span>Product<span>|</span><br>Services<span>|</span>Contact Us<span>|</span><br>FAQs</div>
  <div class="abs vdiv" style="left:814px"></div>
  <div class="abs col" style="left:837px">Connect:
    <div class="social"><span><i></i>chatnest</span><span><i></i>chirplo</span><span><i></i>v+</span><span><i></i>xunmo</span></div>
    <div class="copy">Copyright © 2012. All Rights Reserved.</div></div>
</footer>
</body>
</html>
```